New Business Card Design Project

We are looking for a talented individual to create a truly awesome/unique business card design for us. We are looking for a someone to design something that will really stand out from the crowd - we don't mind what ideas you come up with (ie embossed/flat/matte/shine etc etc) just wow us with your creativity.
Updates

Target Market(s)

Video Games Industry Professionals (all levels of seniority from QA Testers through to CEOs)

Contact Information for Business Card

Company logo (see upload)
Company name: Northbay Play Careers Ltd
Employee Name: Darren Elsby
Job title: CEO
Website: www.nbpc2go.example
Office +44 1632 960418
Mobile: +44 7700 900276
Email: darren@nbpc2go.example

Colors

Designer to choose colors to be used in the design.

Requirements
Must have
• The business card design MUST contain all the information listed in the BUSINESS CARD DETAILS box.
• You will see the colours that are relevant to us (ie company logo) in the uploaded imagery - however you do not have to use all these colours when designing the business card itself
• MUST BE DOUBLE SIDED

```html
<!DOCTYPE html>
<html lang="en">
<head>
<meta charset="utf-8">
<title>Northbay Play Careers – Business Card</title>
<link rel="stylesheet" href="https://fonts.googleapis.com/css2?family=Exo+2:wght@700&family=Montserrat:wght@500;700&display=swap">
<style>
  :root {
    --navy: #1f2f66;
    --navy-soft: #3a4b85;
    --orange: #f28322;
    --paper: #ffffff;
    --backdrop: #232323;
  }
  * { margin: 0; padding: 0; box-sizing: border-box; }
  html, body {
    width: 1200px; height: 1200px; overflow: hidden;
    background: var(--backdrop);
  }
  .canvas {
    position: relative; width: 1200px; height: 1200px;
  }
  .card {
    position: absolute; left: 120px;
    width: 960px; height: 549px;
    background: var(--paper);
    border-radius: 22px;
    overflow: hidden;
  }
  .card--back { top: 34px; }
  .card--front { top: 617px; }

  /* Back side */
  .brand {
    position: absolute; left: 0; right: 0; top: 200px;
    display: flex; align-items: center; justify-content: center; gap: 22px;
  }
  .brand__dot {
    width: 46px; height: 46px; border-radius: 50%;
    background: var(--navy);
  }
  .brand__name {
    font-family: "Exo 2", sans-serif; font-weight: 700;
    font-size: 52px; line-height: 1; color: var(--navy);
  }
  .site {
    position: absolute; left: 0; right: 0;
    text-align: center;
    font-family: "Montserrat", sans-serif; font-weight: 700;
    color: var(--navy);
  }
  .card--back .site { bottom: 70px; font-size: 19px; }

  /* Front side */
  .band {
    position: absolute; right: 0;
  }
  .band--navy { left: 0; top: 300px; height: 170px; background: var(--navy); }
  .band--orange { left: 440px; top: 160px; height: 140px; background: var(--orange); }

  .mascot-area {
    position: absolute; left: 30px; top: 40px;
    width: 400px; height: 460px; border-radius: 18px;
    background: linear-gradient(150deg, var(--navy-soft), var(--navy));
  }
  .front-brand {
    position: absolute; left: 470px; top: 44px;
    font-family: "Exo 2", sans-serif; font-weight: 700;
    font-size: 46px; line-height: 1.05; color: var(--navy);
  }
  .person {
    position: absolute; left: 470px; top: 180px; color: var(--paper);
  }
  .person__name {
    font-family: "Exo 2", sans-serif; font-weight: 700;
    font-size: 44px; line-height: 1.1;
  }
  .person__role {
    font-family: "Exo 2", sans-serif; font-weight: 700;
    font-size: 28px; line-height: 1.2;
  }
  .contacts {
    position: absolute; left: 470px; top: 322px;
    list-style: none; color: var(--paper);
    font-family: "Montserrat", sans-serif; font-weight: 500;
    font-size: 23px;
  }
  .contacts li {
    display: flex; align-items: center; gap: 16px;
    height: 40px;
  }
  .contacts svg { width: 24px; height: 24px; flex: none; }
  .card--front .site { left: 240px; bottom: 26px; font-size: 26px; }
</style>
</head>
<body>
<main class="canvas">

  <section class="card card--back" aria-label="Card back">
    <div class="brand">
      <span class="brand__dot"></span>
      <span class="brand__name">Northbay Play Careers</span>
    </div>
    <p class="site">www.nbpc2go.example</p>
  </section>

  <section class="card card--front" aria-label="Card front">
    <div class="band band--navy"></div>
    <div class="band band--orange"></div>
    <div class="mascot-area" role="img" aria-label="Large brand mascot illustration in navy and white"></div>

    <div class="front-brand">Northbay Play<br>Careers</div>

    <div class="person">
      <p class="person__name">Darren Elsby</p>
      <p class="person__role">CEO</p>
    </div>

    <ul class="contacts">
      <li>
        <svg viewBox="0 0 24 24" aria-hidden="true"><path fill="#f28322" d="M6.6 10.8a15.1 15.1 0 0 0 6.6 6.6l2.2-2.2a1 1 0 0 1 1-.25 11.4 11.4 0 0 0 3.6.57 1 1 0 0 1 1 1V20a1 1 0 0 1-1 1A17 17 0 0 1 3 4a1 1 0 0 1 1-1h3.5a1 1 0 0 1 1 1c0 1.25.2 2.45.57 3.6a1 1 0 0 1-.25 1z"/></svg>
        <span>+44.1632.960418</span>
      </li>
      <li>
        <svg viewBox="0 0 24 24" aria-hidden="true"><rect x="6" y="2" width="12" height="20" rx="2" fill="none" stroke="#f28322" stroke-width="2"/><circle cx="12" cy="18" r="1.3" fill="#f28322"/></svg>
        <span>+44.7700.900276</span>
      </li>
      <li>
        <svg viewBox="0 0 24 24" aria-hidden="true"><rect x="2" y="5" width="20" height="14" rx="1.5" fill="#f28322"/><path d="M3 6l9 7 9-7" fill="none" stroke="#1f2f66" stroke-width="1.6"/></svg>
        <span>darren@nbpc2go.example</span>
      </li>
    </ul>

    <p class="site">www.nbpc2go.example</p>
  </section>

</main>
</body>
</html>
```